Safety Brochure for Industry Assocations

This is an 8.5 x 11 single sided brochure for our Occupational Health and Safety Data Analytics software. If you need to use stock images we will pay for them.

Please incorporate our logo and some of the images. No need to incorporate them all. We like the idea of the boots being at the bottom of the page but we're open to other ideas.

Please note that we intend to mail this brochure to different industries so it should be generic (i.e. not construction specific).

Target Market(s)

Safety and Industry Organisations for construction, mining, forestry and oil and gas industries.

Industry/Entity Type

Industry

Font styles to use
Sans Serif

Colors

Designer to choose colors to be used in the design.

Requirements
Must have
• We are a software company that produces safety software. Our customers are companies that engage in dangerous work and use our software to improve their worker's safety. The look and feel should convey the fact that:
• -We are Big Data
• -We are Software
• -We service industry
Nice to have
• Please see the Pixfold photo of the boots. We were hoping that the desiger would be able ti modify the image with an overlay of 0's and 1's in a kind of "matrix" fashion to indicate that we are merging traditional labour work with software.
Should not have
• No medical symbols. Note that WE ARE NOT HEALTH CARE.

```html
<!DOCTYPE html>
<html lang="en">
<head>
<meta charset="utf-8">
<title>Veltrix Analytics – Industry Data Brochure</title>
<link rel="stylesheet" href="https://fonts.googleapis.com/css2?family=Oswald:wght@500;600&family=Roboto:wght@400;700;900&family=Roboto+Condensed:wght@700&display=swap">
<style>
  :root{
    --green:#12a04a;
    --lime:#8dc63f;
    --charcoal:#4a4646;
    --ink:#111;
    --paper:#fff;
    --backdrop:#000;
  }
  *{margin:0;padding:0;box-sizing:border-box}
  html,body{width:999px;height:1200px;overflow:hidden;background:var(--backdrop)}
  .page{position:absolute;left:84px;top:62px;width:831px;height:1075px;background:var(--paper);overflow:hidden;font-family:"Roboto",Arial,sans-serif}
  .abs{position:absolute}

  .headline-band{left:0;top:30px;width:540px;height:136px}
  .headline{left:32px;top:40px;color:var(--paper);font-family:"Oswald",sans-serif;font-weight:500;line-height:1}
  .headline .line1{font-size:45px;letter-spacing:.5px}
  .headline .line2{font-size:66px;font-weight:600;margin-top:6px}

  .brand{left:574px;top:58px;display:flex;align-items:center;gap:10px}
  .brand .dot{width:70px;height:70px;border-radius:50%;background:var(--green)}
  .brand .name{font-weight:700;font-size:22px;color:var(--charcoal);line-height:1.1}

  .hero{left:0;top:166px;width:831px;height:299px}
  .pillars{left:0;top:166px;width:470px;height:299px}
  .pillar-tag{position:absolute;left:0;height:29px;background:var(--green);clip-path:polygon(0 0,100% 0,calc(100% - 18px) 100%,0 100%);color:var(--paper);font-weight:700;font-size:19px;letter-spacing:.5px;padding-left:37px;line-height:29px}
  .pillar-text{position:absolute;left:36px;color:var(--paper);font-weight:700;font-size:17.5px;letter-spacing:.45px;line-height:24px;white-space:nowrap}

  .callout{position:absolute}
  .callout .tag{height:29px;background:var(--green);clip-path:polygon(0 0,100% 0,calc(100% - 17px) 100%,0 100%);color:var(--paper);font-weight:900;font-size:19px;letter-spacing:.6px;padding-left:5px;line-height:30px}
  .callout .lines{margin-top:8px;font-weight:700;font-size:14.5px;line-height:18.5px;color:var(--ink)}
  .callout .benefit{font-weight:700;font-size:17px;color:var(--green);margin-top:3px}

  .tagline{left:0;top:862px;width:831px;text-align:center;font-family:"Roboto Condensed",sans-serif;font-weight:700;line-height:1}
  .tagline .main{font-size:31px;color:var(--paper)}
  .tagline .main em{font-style:normal;color:var(--lime);font-size:34px}
  .tagline .sub{font-size:31px;color:var(--lime);margin-top:8px}

  .contact{left:0;top:994px;width:831px;text-align:center}
  .phone{display:inline-flex;align-items:center;gap:8px;color:var(--green);font-weight:700;font-size:36px;line-height:1}
  .web{margin-top:6px;font-size:19px;line-height:1;letter-spacing:5px;color:var(--charcoal)}
</style>
</head>
<body>
<main class="page">

  <div class="abs hero" role="img" aria-label="Photo of a hand touching a transparent screen showing charts, percentages and a world map">
    <svg width="831" height="299" viewBox="0 0 831 299">
      <defs>
        <linearGradient id="heroTone" x1="0" y1="0" x2="1" y2="1">
          <stop offset="0" stop-color="#b9c7a0"/>
          <stop offset=".5" stop-color="#7f9170"/>
          <stop offset="1" stop-color="#3e4a3b"/>
        </linearGradient>
      </defs>
      <rect width="831" height="299" fill="url(#heroTone)"/>
      <polygon points="0,0 466,0 351,299 0,299" fill="var(--charcoal)"/>
      <polygon points="466,0 474,0 359,299 351,299" fill="var(--lime)"/>
    </svg>
  </div>

  <svg class="abs headline-band" width="540" height="136" viewBox="0 0 540 136">
    <polygon points="0,0 526,0 471,136 0,136" fill="var(--green)"/>
    <polygon points="526,0 535,0 480,136 471,136" fill="var(--lime)"/>
  </svg>
  <h1 class="abs headline">
    <div class="line1">LEVERAGE THE POWER OF</div>
    <div class="line2">INDUSTRY DATA!</div>
  </h1>

  <div class="abs brand">
    <span class="dot"></span>
    <span class="name">Veltrix<br>Analytics</span>
  </div>

  <section class="abs pillars">
    <div class="pillar-tag" style="top:10px;width:122px">LEAD</div>
    <p class="pillar-text" style="top:43px;left:33px">the next wave of injury reduction</p>
    <div class="pillar-tag" style="top:72px;width:150px">ENGAGE</div>
    <p class="pillar-text" style="top:102px">with members through collaboration and<br>benchmarking</p>
    <div class="pillar-tag" style="top:153px;width:155px">ANALYZE</div>
    <p class="pillar-text" style="top:186px">Accurate, Timely and Complete<br>Leading Indicators</p>
    <div class="pillar-tag" style="top:236px;width:131px;padding-left:28px">TRAIN</div>
    <p class="pillar-text" style="top:265px;left:33px">industry more proactively</p>
  </section>

  <!-- Closing band -->
  <svg class="abs" style="left:0;top:790px" width="831" height="198" viewBox="0 0 831 198">
    <path d="M0,45 Q415,-25 831,45 L831,198 L0,198 Z" fill="var(--charcoal)"/>
  </svg>
  <div class="abs" style="left:305px;top:800px;width:220px;height:180px;background:radial-gradient(ellipse at center,#2a2826 0%,#3a3735 55%,rgba(74,70,70,0) 75%)" role="img" aria-label="Photo of a pair of worn work boots standing on dark ground"></div>

  <!-- Growth arrow, connectors and step markers -->
  <svg class="abs" style="left:0;top:466px" width="831" height="340" viewBox="0 0 831 340">
    <defs>
      <linearGradient id="arrowTone" x1="0" y1="1" x2="1" y2="0">
        <stop offset="0" stop-color="#fff"/>
        <stop offset=".4" stop-color="#cfcfcf"/>
        <stop offset="1" stop-color="#e0e0e0"/>
      </linearGradient>
    </defs>
    <polygon points="330,330 706,192 770,112 746,104 806,72 800,138 788,124 746,198 470,330" fill="url(#arrowTone)"/>
    <polyline points="126,227 326,227 461,262" fill="none" stroke="#9a9a9a" stroke-width="1.5"/>
    <polyline points="174,104 366,104 556,217" fill="none" stroke="#9a9a9a" stroke-width="1.5"/>
    <polyline points="443,50 656,50 656,186" fill="none" stroke="#9a9a9a" stroke-width="1.5"/>
    <circle cx="506" cy="277" r="43" fill="var(--green)"/>
    <rect x="486" y="259" width="40" height="28" fill="none" stroke="#fff" stroke-width="3"/>
    <line x1="506" y1="287" x2="506" y2="299" stroke="#fff" stroke-width="3"/>
    <rect x="494" y="274" width="5" height="9" fill="#fff"/><rect x="503" y="268" width="5" height="15" fill="#fff"/><rect x="512" y="264" width="5" height="19" fill="#fff"/>
    <circle cx="591" cy="237" r="36" fill="var(--green)" stroke="#fff" stroke-width="2"/>
    <rect x="574" y="223" width="34" height="24" fill="none" stroke="#fff" stroke-width="3"/>
    <circle cx="591" cy="235" r="7" fill="#fff"/>
    <circle cx="657" cy="210" r="26" fill="var(--green)"/>
    <polyline points="644,220 651,211 658,216 670,202" fill="none" stroke="#fff" stroke-width="3"/>
    <line x1="642" y1="222" x2="672" y2="222" stroke="#fff" stroke-width="2"/>
  </svg>

  <div class="abs" style="left:29px;top:501px;width:92px;height:92px;border-radius:50%;background:var(--green)"></div>

  <div class="callout" style="left:443px;top:484px">
    <div class="tag" style="width:213px">TREND ANALYSIS</div>
    <div class="lines">Monitor Industry Trends<br>Implement Corrective<br>Initiatives</div>
    <div class="benefit">Improve Safety</div>
  </div>
  <div class="callout" style="left:174px;top:535px">
    <div class="tag" style="width:205px">BENCHMARKING</div>
    <div class="lines">Engage with Members<br>Promote Collaborative<br>Advancement of Safety</div>
    <div class="benefit">Improve Safety</div>
  </div>
  <div class="callout" style="left:126px;top:661px">
    <div class="tag" style="width:198px">TRAINING</div>
    <div class="lines">Analyze needs of Industry<br>Deliver Proactive Training</div>
    <div class="benefit">Improve Safety</div>
  </div>

  <div class="abs tagline">
    <div class="main">The next <em>BIG STEP</em> in injury redcution</div>
    <div class="sub">for your entire industry.</div>
  </div>

  <div class="abs contact">
    <div class="phone">
      <svg width="38" height="38" viewBox="0 0 24 24" aria-hidden="true"><path fill="var(--green)" d="M6.6 10.8c1.4 2.8 3.8 5.1 6.6 6.6l2.2-2.2c.3-.3.7-.4 1-.2 1.1.4 2.3.6 3.6.6.6 0 1 .4 1 1V20c0 .6-.4 1-1 1C10.6 21 3 13.4 3 4c0-.6.4-1 1-1h3.5c.6 0 1 .4 1 1 0 1.3.2 2.5.6 3.6.1.3 0 .7-.2 1z"/><path d="M15 3a6 6 0 0 1 6 6M15 6.5A2.5 2.5 0 0 1 17.5 9" fill="none" stroke="var(--green)" stroke-width="1.8"/></svg>
      1-888-555-0142
    </div>
    <div class="web">www.veltrixanalytics.com</div>
  </div>

  <div class="abs" style="left:0;top:1064px;width:411px;height:11px;background:var(--charcoal)"></div>
  <div class="abs" style="left:411px;top:1064px;width:420px;height:11px;background:var(--green)"></div>
</main>
</body>
</html>
```